opening page for professional healing and psychology program

wordpress opening page that can be inserted in already existing design for the back end, but with a new look for the splash page. Our company is about consciousness, being grounded and doing good work in the world, learning energy healing and depth psychology - not interested in the typical lotus flowers or chakras etc. I have included design elements I am interested in working with and would love your help making it all work together. The side bar, listed below as "old bravecrest splash page" (to see it as it is online now, bravecrestacademy.example) on the right MUST BE INCLUDED on the page, but can be reformatted to work with new design. I am interested in bright colors and a sense of aliveness. There is a video for the page, youtube link included https://videohost.example/watch/Qm7TzWp4RkA
Updates

In the bottom three boxes for the page, I need to replace the BLOG section with this photo andTHE ORIGINAL ONGOING HEALERS'FORUMDeborah Allen and Rob Tarkett and photo I am trying to load into the brief called m and r africa Added Saturday, April 22, 2017

Target Market(s)

mid-life professionals in the healing arts including acupuncturists, nurses, doctors, therapists, hands on energy workers, etc.

Industry/Entity Type

Health And Wellness

Colors

Designer to choose colors to be used in the design.

Requirements
Must have
• Originality, color, and welcome
Nice to have
• dynamic alive design that draws you in to growth and change and curiosity
• integrate with colors in logo
Should not have
• chakras, lotus flowers, typical mediation site stuff

```html
<!DOCTYPE html>
<html lang="en">
<head>
<meta charset="utf-8">
<title>Bravecrest Institute – Home</title>
<link href="https://fonts.googleapis.com/css2?family=Montserrat:wght@400;600;700&family=Open+Sans:wght@400;600;700&display=swap" rel="stylesheet">
<style>
:root{
  --navy:#1f2340;
  --navy-2:#2b3150;
  --red:#d7322c;
  --red-deep:#b9221f;
  --gold:#f2b233;
  --text:#3a3a3a;
  --muted:#9a9a9a;
  --white:#ffffff;
  --line:#e2e2e2;
}
*{box-sizing:border-box;margin:0;padding:0}
html,body{width:1200px;height:3041px;overflow:hidden}
body{font-family:"Open Sans",Arial,sans-serif;color:var(--text);background:var(--white);position:relative}
section,header,footer{position:relative;width:1200px;overflow:hidden}

/* top bar */
.topbar{height:45px;background:var(--navy)}
.topbar .social{position:absolute;left:108px;top:14px;display:flex;gap:14px}
.topbar .social span{width:14px;height:14px;background:#c9ccd8;border-radius:2px}
.topbar .phone{position:absolute;left:886px;top:0;width:214px;height:45px;background:var(--red);color:var(--white);font:600 21px "Montserrat",sans-serif;display:flex;align-items:center;gap:16px;padding-left:18px}

/* header */
.site-header{height:121px;background:var(--white)}
.brand{position:absolute;display:flex;align-items:center;gap:10px;font-family:"Montserrat",sans-serif;font-weight:600;white-space:nowrap}
.brand .mark{flex:none;width:58px;height:58px;border-radius:50%;background:var(--navy-2)}
.brand-institute{left:101px;top:28px;font-size:21px;line-height:23px;color:var(--navy-2)}
.brand-forum{left:334px;top:38px;font-size:28px;color:var(--red)}
.brand-forum .mark{width:44px;height:44px;background:var(--gold)}
.main-nav{position:absolute;right:96px;top:50px;display:flex;gap:52px;font:700 12px "Montserrat",sans-serif;color:#111;letter-spacing:.3px}

/* hero */
.hero{height:428px;background:linear-gradient(135deg,#6b5a3f,#a68a5d 40%,#8a7352 70%,#4c4232)}
.hero .panel{position:absolute;inset:0}
.hero p{position:absolute;left:693px;top:132px;width:350px;color:var(--white);font:600 19px/31px "Open Sans",sans-serif}

/* section titles */
.sec-title{font:700 29px "Montserrat",sans-serif;text-align:center;color:var(--red)}
.sec-title em{font-style:normal;color:var(--gold)}
.sec-title::after{content:"";display:block;width:34px;height:3px;background:var(--red);margin:16px auto 0}

/* we are */
.we-are{height:318px}
.we-are .sec-title{position:absolute;left:0;right:0;top:36px}
.we-are h3{position:absolute;top:108px;left:0;right:0;text-align:center;color:var(--red);font:400 23px "Open Sans",sans-serif}
.we-are p{position:absolute;top:148px;left:140px;right:140px;text-align:center;font-size:15px;line-height:28px}
.btn-more{position:absolute;left:523px;top:226px;width:154px;height:42px;border-radius:21px;background:var(--navy-2);color:var(--white);font:700 12px "Montserrat",sans-serif;letter-spacing:1px;display:flex;align-items:center;padding-left:46px}
.btn-more::before{content:"";position:absolute;left:5px;top:5px;width:32px;height:32px;border-radius:50%;background:var(--gold);border:3px solid var(--white)}

/* what we do */
.what-we-do{height:472px;background:radial-gradient(ellipse at 60% 40%,#e04a3b,var(--red) 45%,var(--red-deep))}
.what-we-do h2{position:absolute;left:101px;top:42px;color:var(--white);font:700 27px "Montserrat",sans-serif}
.what-we-do h2 em{font-style:normal;color:var(--gold)}
.what-we-do .rule{position:absolute;left:101px;top:92px;width:578px;height:1px;background:rgba(255,255,255,.45)}
.benefits{position:absolute;left:101px;top:120px;width:630px;list-style:none}
.benefits li{position:relative;padding-left:52px;color:var(--white);font-size:16px;line-height:24px;margin-bottom:20px}
.benefits li b{font-weight:700}
.benefits li::before{content:"";position:absolute;left:0;top:4px;width:28px;height:24px;border:2px solid var(--white);border-radius:50% 50% 6px 6px}
.what-we-do .figure{position:absolute;left:811px;top:10px;width:290px;height:450px;border-radius:40% 40% 10% 10%;background:linear-gradient(160deg,#5b4a44,#2b3558 55%,#1f2a48)}

/* events */
.events{height:284px}
.events .sec-title{position:absolute;left:0;right:0;top:44px}
.event{position:absolute;top:140px;width:480px}
.event.left{left:99px}.event.right{left:643px}
.date{position:absolute;left:0;top:0;width:56px;height:56px;text-align:center;font-family:"Montserrat",sans-serif}
.date .d{display:block;height:34px;background:var(--navy-2);color:var(--white);font-size:26px;line-height:34px}
.date .m{display:block;height:22px;background:var(--red);color:var(--white);font-size:13px;font-weight:700;line-height:22px}
.event h4{margin-left:74px;font:600 17px "Montserrat",sans-serif;color:var(--navy);white-space:nowrap}
.event .when{margin-left:74px;color:var(--red);font-size:16px;margin-top:4px}
.event .sum{margin-left:74px;width:330px;color:#b0b0b0;font-size:13px;line-height:22px;margin-top:4px}
.event .sum span{color:var(--red)}
.events .divider{position:absolute;left:594px;top:136px;width:1px;height:112px;background:var(--line)}

/* coffee */
.coffee{height:325px;background:linear-gradient(90deg,#1e3552,#2d4a6b 40%,#2a3c57)}
.coffee .art{position:absolute;left:41px;top:0;width:506px;height:325px;background:radial-gradient(circle at 50% 38%,#4d7fb2 0,#2e5878 24%,#25465e 40%,transparent 70%)}
.coffee .tag{position:absolute;left:122px;top:272px;color:var(--white);font:700 26px "Montserrat",sans-serif}
.coffee h2{position:absolute;left:570px;top:34px;color:var(--white);font:600 27px "Montserrat",sans-serif}
.coffee .rule{position:absolute;left:570px;top:80px;width:532px;height:1px;background:rgba(255,255,255,.4)}
.coffee .lead{position:absolute;left:570px;top:94px;width:530px;color:#dfe4ec;font-size:14px;line-height:22px}
.coffee .body{position:absolute;left:570px;top:146px;width:530px;color:#b8c0cd;font-size:12.5px;line-height:22px}

/* about */
.about{height:328px;background:linear-gradient(180deg,#fff 0,#fff 40%,#efe9e1 75%,#e6ddd0)}
.about h2{position:absolute;left:101px;top:44px;color:var(--navy);font:700 28px "Montserrat",sans-serif}
.about .rule{position:absolute;left:101px;top:82px;width:510px;height:2px;background:linear-gradient(90deg,var(--red),#ccc)}
.about .lead{position:absolute;left:101px;top:94px;width:520px;font-size:14px;line-height:22px;color:#444}
.about .body{position:absolute;left:101px;top:148px;width:530px;font-size:12.5px;line-height:22px;color:#888}
.about .photo{position:absolute;left:780px;top:34px;width:335px;height:294px;background:linear-gradient(180deg,#d8cbb5,#b6a283 50%,#6a5a4c)}

/* testimonials */
.stories{height:339px}
.stories .arrow{position:absolute;top:118px}
.video{position:absolute;top:30px;width:306px}
.video .frame{height:195px;background:linear-gradient(150deg,#d9d4cc,#a8a099 60%,#5e5a57);position:relative}
.video .play{position:absolute;left:129px;top:72px;width:48px;height:48px;border-radius:50%;background:var(--navy-2)}
.video .bar{position:absolute;left:0;right:0;bottom:0;height:14px;background:#111}
.video p{margin-top:12px;font-size:12.5px;line-height:21px;color:#333}

/* newsletter */
.newsletter{height:89px;background:var(--red)}
.newsletter .label{position:absolute;left:106px;top:34px;color:var(--white);font:700 14px "Open Sans",sans-serif}
.newsletter .field{position:absolute;left:400px;top:26px;width:300px;height:34px;border:1px solid #ef8a84;background:#c72a24;color:#f7c9c6;font-size:12px;padding:9px 12px}
.newsletter .btn{position:absolute;left:708px;top:26px;width:104px;height:34px;background:var(--navy-2);color:var(--white);font:600 14px "Open Sans",sans-serif;text-align:center;line-height:34px}
.newsletter .social{position:absolute;left:883px;top:26px;display:flex;gap:10px}
.newsletter .social span{width:32px;height:32px;background:var(--navy-2)}

/* footer */
.site-footer{height:247px;background:linear-gradient(90deg,#2a2f47,#3a3f57 60%,#2a2f47)}
.site-footer h5{position:absolute;top:30px;color:var(--white);font:600 15px "Open Sans",sans-serif}
.site-footer h5::after{content:"";display:block;width:80px;height:1px;background:rgba(255,255,255,.4);margin-top:10px}
.quick{position:absolute;left:101px;top:68px;list-style:none}
.quick li{color:#dfe1e8;font-size:11.5px;height:33px;line-height:33px;padding-left:12px;position:relative;border-bottom:1px solid rgba(255,255,255,.08);width:100px}
.quick li::before{content:"›";position:absolute;left:0;color:var(--red)}
.contact{position:absolute;left:290px;top:70px;list-style:none}
.contact li{color:#dfe1e8;font-size:11px;line-height:16px;margin-bottom:17px;padding-left:16px;position:relative}
.contact li::before{content:"";position:absolute;left:0;top:4px;width:7px;height:7px;border-radius:50%;background:var(--red)}
.foot-brand{position:absolute;display:flex;align-items:center;gap:10px;font:600 22px/24px "Montserrat",sans-serif;color:rgba(255,255,255,.35);white-space:nowrap}
.foot-brand .mark{flex:none;width:64px;height:64px;border-radius:50%;background:rgba(255,255,255,.18)}
.foot-institute{left:548px;top:86px}
.foot-forum{left:805px;top:104px;font-size:26px}
.copyright{height:45px;background:var(--navy);color:#c9ccd8;font-size:12px;text-align:center;line-height:45px}
</style>
</head>
<body>

<div class="topbar">
  <div class="social"><span></span><span></span><span></span><span></span><span></span></div>
  <div class="phone">
    <svg width="20" height="20" viewBox="0 0 24 24"><rect x="1" y="1" width="22" height="22" rx="3" fill="#fff"/><path d="M8 6l2 3-1.5 1.5a8 8 0 0 0 5 5L15 14l3 2-1 2.5C11 18 6 13 5.5 7z" fill="#d7322c"/></svg>
    (555)014-2870
  </div>
</div>

<header class="site-header">
  <div class="brand brand-institute"><span class="mark"></span><span>Bravecrest<br>Institute</span></div>
  <div class="brand brand-forum"><span class="mark"></span>Menders'Circle</div>
  <nav class="main-nav"><span>ABOUT US</span><span>WHAT WE OFFER</span><span>SHOP</span><span>CONTACT</span></nav>
</header>

<section class="hero" role="img" aria-label="Sunlit photograph of an old wooden gate opening onto a stone path">
  <svg class="panel" width="1200" height="428"><polygon points="640,0 1200,0 1200,428 588,428" fill="#23273f" fill-opacity=".82"/></svg>
  <p>in the summer of 2017, The Bravecrest Institute transitioned to the care of Senior Faculty Marisol Penhale and the Menders' Circle. Please continue to travel with us on this new part of the journey.</p>
</section>

<section class="we-are">
  <h2 class="sec-title">We <em>Are</em></h2>
  <h3>Committed to resilience, commitment, support &amp; love</h3>
  <p>We are &nbsp;a program for lifelong learners in consciousness, healing, energy work, and depth psychology a place to grow with a community of people working to create or enhance careers in the healing arts</p>
  <div class="btn-more">READ MORE</div>
</section>

<section class="what-we-do">
  <h2>What We Do <em>Together</em></h2>
  <div class="rule"></div>
  <ul class="benefits">
    <li>Develop the skills needed to <b>successfully facilitate healing for<br>yourself and others</b></li>
    <li>Improve and <b>deepen your relationships</b> by understanding the ever<br>more complex patterns of why we do what we do and feel what we feel</li>
    <li>Enjoy <b>better health and vitality</b> for yourself and give that gift to<br>others</li>
    <li><b>Cultivate your natural healing abilities</b> with a supportive community</li>
    <li><b>Make a living doing what you love</b> without draining yourself or your<br>bank account</li>
  </ul>
  <div class="figure" role="img" aria-label="Painted illustration of a winged figure in a blue dress"></div>
</section>

<section class="events">
  <h2 class="sec-title">Upcoming <em>Events</em></h2>
  <div class="event left">
    <div class="date"><span class="d">30</span><span class="m">NOV</span></div>
    <h4>Level 1 Body Mind Balance Certification</h4>
    <div class="when">November 30-December 3, 2017</div>
    <div class="sum">Lorem ipsum dolor sit consectetuer adipiscing elit sed diam nonummy nibh euismod <span>(+)</span></div>
  </div>
  <div class="divider"></div>
  <div class="event right">
    <div class="date"><span class="d">15</span><span class="m">JAN</span></div>
    <h4>Level 2 Energy Healing Counselor Certification</h4>
    <div class="when">January 15-January 20, 2018</div>
    <div class="sum">Lorem ipsum dolor sit consectetuer adipiscing elit sed diam nonummy nibh euismod <span>(+)</span></div>
  </div>
</section>

<section class="coffee">
  <div class="art" role="img" aria-label="Illustration of the Earth with white wings standing in boots above mountains under a night sky"></div>
  <div class="tag">Deper Roots - Wider Wings</div>
  <h2>Coffee with Marisol Penhale</h2>
  <div class="rule"></div>
  <p class="lead">Lorem ipsum dolor sit amet, consectetuer adipiscing elit, sed diam nonummy nibh euismod tincidunt ut laoreet</p>
  <p class="body">Ut wisi enim ad minim veniam, quis nostrud exerci tation ullamcorper suscipit lobortis nisl ut aliquip ex ea commodo consequat. Duis autem vel eum iriure dolor in hendrerit in vulputate velit esse molestie consequat, vel illum dolore eu feugiat nulla facilisis at vero eros et accumsan et iusto odio dignissim qui blandit praesent luptatum zzril delenit augue duis dolore te feugait nulla facilisi.Ut wisi enim ad minim veniam, quis nostrud exerci tation ullamcorper suscipit lobortis nisl</p>
</section>

<section class="about">
  <h2>ABOUT US</h2>
  <div class="rule"></div>
  <p class="lead">Lorem ipsum dolor sit amet, consectetuer adipiscing elit, sed diam nonummy nibh euismod tincidunt ut laoreet</p>
  <p class="body">Ut wisi enim ad minim veniam, quis nostrud exerci tation ullamcorper suscipit lobortis nisl ut aliquip ex ea commodo consequat. Duis autem vel eum iriure dolor in hendrerit in vulputate velit esse molestie consequat, vel illum dolore eu feugiat nulla facilisis at vero eros et accumsan et iusto odio dignissim qui blandit praesent luptatum zzril delenit augue duis dolore te feugait nulla facilisi.Ut</p>
  <div class="photo" role="img" aria-label="Photograph of the two program founders standing outdoors on a grassy plain"></div>
</section>

<section class="stories">
  <svg class="arrow" style="left:70px" width="14" height="24"><path d="M11 2 3 12l8 10" fill="none" stroke="#2b3150" stroke-width="2"/></svg>
  <svg class="arrow" style="left:1116px" width="14" height="24"><path d="M3 2l8 10-8 10" fill="none" stroke="#2b3150" stroke-width="2"/></svg>
  <div class="video" style="left:99px">
    <div class="frame" role="img" aria-label="Video still of a student speaking beside an institute sign"><span class="play"></span><svg style="position:absolute;left:147px;top:86px" width="16" height="20"><path d="M0 0l16 10L0 20z" fill="#fff"/></svg><span class="bar"></span></div>
    <p>"I was looking to recreate myself. I was looking for my purpose in my life. I am already making money as an Energy Healer and I just finished Level 1."</p>
  </div>
  <div class="video" style="left:448px">
    <div class="frame" role="img" aria-label="Video still of a student speaking beside an institute sign"><span class="play"></span><svg style="position:absolute;left:147px;top:86px" width="16" height="20"><path d="M0 0l16 10L0 20z" fill="#fff"/></svg><span class="bar"></span></div>
    <p>"Before I went to Bravecrest, I struggled with getting pregnant, it wasn't happening..."</p>
  </div>
  <div class="video" style="left:797px">
    <div class="frame" role="img" aria-label="Video still of a student speaking in a lamp-lit room"><span class="play"></span><svg style="position:absolute;left:147px;top:86px" width="16" height="20"><path d="M0 0l16 10L0 20z" fill="#fff"/></svg><span class="bar"></span></div>
    <p>"A friend said, 'People don't change.' But I was able to communicate to him, people do change. I've changed, because of this."</p>
  </div>
</section>

<section class="newsletter">
  <div class="label">Stay updated with latest news from</div>
  <div class="field">Enter Your Email</div>
  <div class="btn">Subscribe</div>
  <div class="social"><span></span><span></span><span></span><span></span><span></span></div>
</section>

<footer class="site-footer">
  <h5 style="left:101px">Quick Links</h5>
  <ul class="quick"><li>Home</li><li>About Us</li><li>What We Offer</li><li>Shop</li><li>Contact</li></ul>
  <h5 style="left:290px">Contact Details</h5>
  <ul class="contact">
    <li>Bravecrest Institute. P.O. Box 4410-200,<br>Alder Glen, CA 90000</li>
    <li>Information: (555) 013-4471</li>
    <li>Registration: (555) 019-2236</li>
    <li>office@bravecrestacademy.example</li>
  </ul>
  <div class="foot-brand foot-institute"><span class="mark"></span><span>Bravecrest<br>Institute</span></div>
  <div class="foot-brand foot-forum">Menders'Circle</div>
</footer>
<div class="copyright">Copyright © 2017 - Bravecrest Institute of Transpersonal Energy Healing. All Rights Reserved.</div>

</body>
</html>
```